Regional beer Moltan-Bräu needs new labels for 33cl Beercans

We are looking for a creative and professional design for our 33cl beer can label. The can itself is all black, and the design should be mainly in yellow and black colors to stand out on the store shelf.
The size of the label should be 206 mm x 80 mm

*Details and requirements:*

1. brand identity and target group
- Our brand stands for handcrafted quality with a modern touch.
- The target group is young adults and beer connoisseurs who value unique taste and stylish design.

2. style and aesthetics:*
- The design should be modern and eye-catching, inspired by the labels of Kelvo Brauerei Hamburg.
- We prefer a minimalist style with clean lines and contrasts.

3. typography:*
- Use modern, legible fonts.
- Use freely available fonts.
- The brand name and important information should be emphasized.

4. images and graphics
- The logo can be used in its entirety or in individual parts.
- Illustrations or icons that emphasize the uniqueness of our beer are welcome.

5 *Colors:*
- Main colors are yellow and black.
- Accents in other colors are possible, but should be used sparingly.

6th *Legal requirements:*
- The label must provide space for legal information such as alcohol content, origin and barcode.

7 *Technical details
- Final files should be in AI, afdesign or PDF format with a resolution of at least 300 dpi.
- The design should be created in CMYK color model.

8th *Inspiration and references:*
- Examples of labels that we like are those of Kelvo Brauerei Hamburg. We like their clear structure and modern look.

9 *Additional information:*
- The bottling date is printed on the can or bottle afterwards.
- Special features of our beer, such as flavor or special ingredients, should be highlighted.

We look forward to your creative suggestions and hope that you will help us to design a label that perfectly represents our brand!

Target Market(s)

The target group is young adults and beer connoisseurs who value unique taste and stylish design.

Industry/Entity Type

Beverage

Colors

Requirements
Must have
• The design should be modern and eye-catching but minimalist style with clean lines and contrasts. should include the writing moltan-bräu (attachment)

```html
<!DOCTYPE html>
<html lang="de">
<head>
<meta charset="utf-8">
<title>Moltan-Bräu Helles – Dosenetikette 33cl</title>
<link rel="stylesheet" href="https://fonts.googleapis.com/css2?family=Alfa+Slab+One&family=Arimo:wght@700&family=Tinos:wght@700&display=swap">
<style>
  :root {
    --yellow: #f7c21f;
    --black: #050505;
    --panel: #141416;
    --white: #ffffff;
    --hop: #3a3a3c;
    --fresh-red: #e0352b;
    --fresh-orange: #f39a1d;
    --fresh-green: #6cc43c;
  }
  html, body { margin: 0; padding: 0; overflow: hidden; }
  body { width: 1200px; height: 1200px; }
  .presentation { display: block; width: 1200px; height: 1200px; }
  .seal-text { font-family: "Tinos", "Times New Roman", serif; font-weight: 700; fill: var(--white); }
  .style-name { font-family: "Alfa Slab One", Georgia, serif; fill: var(--black); font-size: 56px; }
  .info { font-family: "Arimo", Arial, sans-serif; font-weight: 700; fill: var(--white); font-size: 15px; }
  .info-large { font-size: 17px; }
  .volume { font-size: 30px; }
  .legal { font-family: "Arimo", Arial, sans-serif; font-weight: 700; fill: var(--black); font-size: 10px; }
</style>
</head>
<body>
<svg class="presentation" viewBox="0 0 1500 1500" xmlns="http://www.w3.org/2000/svg" xmlns:xlink="http://www.w3.org/1999/xlink">
  <defs>
    <linearGradient id="freshness" x1="0" y1="0" x2="0" y2="1">
      <stop offset="0" stop-color="var(--fresh-red)"/>
      <stop offset="0.13" stop-color="var(--fresh-orange)"/>
      <stop offset="0.22" stop-color="var(--fresh-orange)"/>
      <stop offset="0.27" stop-color="var(--fresh-green)"/>
      <stop offset="1" stop-color="var(--fresh-green)"/>
    </linearGradient>
    <path id="arc-top" d="M333 367 A195 195 0 0 1 723 367"/>
    <path id="arc-bottom" d="M340.9 334 A190 190 0 1 0 715.1 334"/>

    <g id="can-label">
      <!-- outer band -->
      <rect x="165" y="160" width="1170" height="417" rx="42" fill="var(--yellow)"/>
      <rect x="175" y="171" width="1150" height="395" rx="34" fill="var(--white)"/>
      <rect x="181" y="178" width="1138" height="381" rx="28" fill="var(--yellow)"/>

      <!-- info panel -->
      <rect class="info-panel" x="712" y="181" width="548" height="376" fill="var(--panel)"/>
      <rect x="1260" y="181" width="23" height="376" fill="var(--white)"/>
      <rect class="freshness-bar" x="1284" y="181" width="16" height="376" fill="url(#freshness)"/>
      <path d="M1284 341 L1294 349 L1284 357 Z" fill="var(--black)"/>

      <rect role="img" aria-label="Hopfendolde als dezente Hintergrundillustration" x="940" y="222" width="170" height="300" rx="70" fill="var(--hop)" opacity="0.55"/>

      <!-- seal -->
      <rect x="345" y="99" width="368" height="551" fill="var(--yellow)"/>
      <circle cx="528" cy="367" r="272" fill="var(--white)"/>
      <circle cx="528" cy="367" r="264" fill="var(--yellow)"/>
      <circle cx="528" cy="367" r="254" fill="var(--black)"/>

      <text class="seal-text" font-size="64" letter-spacing="2"><textPath xlink:href="#arc-top" startOffset="50%" text-anchor="middle">MOLTAN-BRÄU</textPath></text>
      <text class="seal-text" font-size="62" letter-spacing="3"><textPath xlink:href="#arc-bottom" startOffset="50%" text-anchor="middle">DOSEN ETIKETTE</textPath></text>
      <text class="seal-text" x="528" y="400" font-size="96" text-anchor="middle">33CL</text>

      <!-- style name -->
      <text class="style-name" transform="translate(246 375) rotate(-90) scale(1 1.15)" text-anchor="middle">HELLES</text>

      <!-- info texts -->
      <text class="info" text-anchor="middle">
        <tspan x="877" y="221">Guets Bier wird nid schlächt!</tspan>
        <tspan x="877" y="240">Steu’s aber ane dunkle Ort</tspan>
        <tspan x="877" y="259">ad Chüeli</tspan>
        <tspan x="885" y="317">Besser wird’s im Auter</tspan>
        <tspan x="885" y="335">de nid</tspan>
        <tspan x="885" y="392">Jedi Fläschä isch</tspan>
        <tspan x="885" y="410">äs Unikat.</tspan>
        <tspan x="885" y="428">Vo Hand u mit viu</tspan>
        <tspan x="885" y="446">Ufwand brauet</tspan>
        <tspan x="876" y="511">Für Allergiker</tspan>
        <tspan x="876" y="529">jeglicher Art:</tspan>
        <tspan x="876" y="547">Löt’s besser grad la si</tspan>
      </text>
      <text class="info info-large" text-anchor="middle">
        <tspan x="1151" y="223">Brauerei:</tspan>
        <tspan x="1151" y="244">Moltan-Bräu</tspan>
        <tspan x="1151" y="265">Talgasse 12</tspan>
        <tspan x="1151" y="286">CH-3345 Wendlingen</tspan>
        <tspan x="1151" y="317">www.moltan-bräu.ch</tspan>
      </text>
      <text class="info" text-anchor="middle">
        <tspan x="1138" y="458">Zutaten:</tspan>
        <tspan x="1138" y="478">Wasser, Gerstenmalz</tspan>
        <tspan x="1138" y="498">Hopfen, Hefe</tspan>
      </text>
      <text class="info" x="1048" y="548">Alc. 4.8% vol.</text>
      <text class="info volume" x="1161" y="546">33cl</text>

      <!-- legal strip -->
      <text class="legal" transform="translate(1274 557) rotate(-90)">Mindestens haltbar bis: 10.10.2025</text>
      <text class="legal" transform="translate(1274 264) rotate(-90)">W-LOS: W181</text>
    </g>
  </defs>

  <rect class="backdrop-light" x="0" y="0" width="1500" height="750" fill="var(--white)"/>
  <rect class="backdrop-dark" x="0" y="750" width="1500" height="750" fill="var(--black)"/>

  <use xlink:href="#can-label"/>
  <use xlink:href="#can-label" transform="translate(0 743)"/>
</svg>
</body>
</html>
```